bottle label/ product label for smoothies (ultra fresh)

Please create a bottle label for our smoothies for retail distribution.
It's important that the following key features are clearly stated:

Ultra-fresh

Handmade

No preservatives

Not heat-treated

No added sugar

The base of the product label should be transparent, so that the color and content of the smoothie can be seen clearly.

We are a young, dynamic company. Our values are honesty, ultra-freshness, and authenticity — and we are the only ones producing this type of product in our country. We are positioned in the premium segment.

Design style: Modern, clean, and natural — but not playful or childish.

Example product: Kelu Kelu (Mango, Pineapple, Lemon, Passion Fruit, Orange)

Wenn du möchtest, kann ich auch gleich einen konkreten Vorschlag für das Etikettendesign auf Englisch oder einen Entwurfstext für das Label selbst erstellen. Sag einfach Bescheid!

Target Market(s)

trade - convenience

Industry/Entity Type

trade

Font styles to use
Sans Serif

Requirements
Must have
• sales- features: Ultra-fresh Handmade No preservatives Not heat-treated No added sugar

```html
<!DOCTYPE html>
<html lang="en">
<head>
<meta charset="utf-8">
<title>Kelu Kelu – Smoothie Label</title>
<link rel="stylesheet" href="https://fonts.googleapis.com/css2?family=Barlow:wght@500;600&family=Barlow+Condensed:wght@500;600;700&display=swap">
<style>
  :root {
    --smoothie-light: #fdd22c;
    --smoothie-mid: #f7c018;
    --smoothie-deep: #eeac0a;
    --label-ink: #ffffff;
  }
  html, body {
    margin: 0;
    padding: 0;
    width: 1200px;
    height: 1200px;
    overflow: hidden;
  }
  .label-canvas {
    display: block;
    width: 1200px;
    height: 1200px;
  }
  .brand-name {
    font-family: "Barlow", sans-serif;
    font-weight: 600;
    font-size: 48px;
    fill: var(--label-ink);
  }
  .brand-tagline {
    font-family: "Barlow", sans-serif;
    font-weight: 500;
    font-size: 26px;
    letter-spacing: 6px;
    fill: var(--label-ink);
  }
  .product-name {
    font-family: "Barlow Condensed", sans-serif;
    font-weight: 700;
    font-size: 135px;
    fill: var(--label-ink);
  }
  .divider {
    fill: var(--label-ink);
  }
  .ingredient {
    font-family: "Barlow Condensed", sans-serif;
    font-weight: 600;
    font-size: 18px;
    letter-spacing: 2.5px;
    fill: var(--label-ink);
  }
  .freshness-claim {
    font-family: "Barlow Condensed", sans-serif;
    font-weight: 500;
    font-size: 22px;
    fill: var(--label-ink);
  }
  .promise-box {
    fill: none;
    stroke: var(--label-ink);
    stroke-width: 2;
  }
  .promise-no {
    font-family: "Barlow Condensed", sans-serif;
    font-weight: 700;
    font-size: 62px;
    fill: var(--label-ink);
  }
  .promise-item {
    font-family: "Barlow Condensed", sans-serif;
    font-weight: 600;
    font-size: 20px;
    fill: var(--label-ink);
  }
</style>
</head>
<body>
<svg class="label-canvas" viewBox="0 0 1200 1200" xmlns="http://www.w3.org/2000/svg">
  <defs>
    <linearGradient id="smoothie-fill" x1="0" y1="0" x2="1" y2="0">
      <stop offset="0" stop-color="var(--smoothie-light)"/>
      <stop offset="0.5" stop-color="var(--smoothie-mid)"/>
      <stop offset="1" stop-color="var(--smoothie-deep)"/>
    </linearGradient>
  </defs>

  <rect class="smoothie-background" x="0" y="0" width="1200" height="1200" fill="url(#smoothie-fill)"/>

  <g class="label" transform="translate(-586,-702) scale(1.4)">
    <g class="brand">
      <text class="brand-name" x="840" y="572" text-anchor="middle">Solvida</text>
      <text class="brand-tagline" x="842" y="618" text-anchor="middle">handmade</text>
    </g>

    <text class="product-name" transform="translate(783,1330) rotate(-90)" x="0" y="0" textLength="655" lengthAdjust="spacing">KELU-KELU</text>

    <rect class="divider" x="815" y="678" width="6" height="648"/>

    <g class="ingredients">
      <text class="ingredient" x="849" y="695">MANGO</text>
      <text class="ingredient" x="849" y="762">LEMON</text>
      <text class="ingredient" x="849" y="829">ORANGE</text>
      <text class="ingredient" x="849" y="896">PINEAPPLE</text>
      <text class="ingredient" x="849" y="962">PASSION FRUIT</text>
    </g>

    <text class="freshness-claim" transform="translate(877,1325) rotate(-90)" x="0" y="0" textLength="288" lengthAdjust="spacing">ULTRA-FRESH</text>

    <g class="promises">
      <rect class="promise-box" x="906" y="1042" width="99" height="284"/>
      <text class="promise-no" transform="translate(987,1286) rotate(-90)" x="0" y="0" textLength="82" lengthAdjust="spacingAndGlyphs">NO</text>
      <text class="promise-item" transform="translate(937,1196) rotate(-90)" x="0" y="0" textLength="124" lengthAdjust="spacingAndGlyphs">preservatives</text>
      <text class="promise-item" transform="translate(959,1196) rotate(-90)" x="0" y="0" textLength="121" lengthAdjust="spacingAndGlyphs">heat-treated</text>
      <text class="promise-item" transform="translate(982,1196) rotate(-90)" x="0" y="0" textLength="117" lengthAdjust="spacingAndGlyphs">added sugar</text>
    </g>
  </g>
</svg>
</body>
</html>
```